Northwind Crown Hair Supply needs a packaging design

We need a packaging design for a new hair extension company based in Edmonton, Alberta called Velvet Strands. Our packaging should communicate high quality, luxurious hair that will never tangle or dry out. The product will be marketed to salon professionals as well as clients. There must be an opening to see the hair from the outside.

Our advertising campaign is going to be based on boho chic; Dorian Keswick/ Open Meadow/Tumbling Echo.

Target Market(s)

Women and beauty industry professionals. High end market.

Industry/Entity Type

Advertising

Requirements
Must have
• "Highest quality 100% Remi hair!" should be written on the front of the package. In addition, we would like to add text to the back or inside of the packaging as follows:
• Hair Collection and Color Processing:
• Only the highest quality hair is selected which ensures high moisture and nutrient content
• The hair is directly cut from the donor which ensures that the hair cuticle remains intact and always tangle-free
• No chemicals are used in dyeing the hair
• The hair will never fade due to the mild and healthy herbal extract used in the dyeing process which gently penetrates to the inner core of the hair
• Care Instructions:
• Velvet Strands provides only the highest in quality Remi hair that demands very little care to maintain it’s luxurious feel.
• Use a proper extension bristle brush
• Wash the hair with a sulfate-free shampoo and follow with a moisturizing conditioner that is formulated for hair extensions
• Do not apply any type of chemicals to the hair
• We proudly show our immense passion for delivering superior quality in our full product line.
• We insist that it is important for you to know and understand what you are purchasing in your hair extensions. We guarantee the highest quality of our products.
• Velvet Strands is strongly committed to serving their clients with utmost integrity, believing in a foundation of personal and professional ethics and our 20 years service in the beauty industry.

```html
<!DOCTYPE html>
<html lang="en">
<head>
<meta charset="utf-8">
<title>Velvet Strands – Packaging</title>
<link rel="stylesheet" href="https://fonts.googleapis.com/css2?family=Open+Sans:wght@300;400;600;700&display=swap">
<style>
  :root {
    --stage: #efefef;
    --box-dark: #141a21;
    --spine-dark: #10151b;
    --wave-dark: #27313c;
    --accent-red: #e0193f;
    --accent-white: #ffffff;
    --hair-deep: #241820;
    --hair-mid: #4a3442;
    --text-light: #ffffff;
  }
  html, body {
    margin: 0;
    width: 1200px;
    height: 1200px;
    overflow: hidden;
    background: var(--stage);
    font-family: "Open Sans", sans-serif;
  }
  .package {
    position: absolute;
    left: 325px;
    top: 100px;
    display: flex;
    height: 1000px;
    box-shadow: 0 20px 40px rgba(0,0,0,0.18);
  }
  .package-spine { width: 110px; height: 1000px; display: block; }
  .package-front { width: 440px; height: 1000px; display: block; }
  .panel-bg { fill: var(--box-dark); }
  .spine-bg { fill: var(--spine-dark); }
  .brand-name { fill: var(--text-light); font-family: "Open Sans", sans-serif; font-weight: 400; }
  .tagline-bold { fill: var(--text-light); font-weight: 600; }
  .tagline-light { fill: var(--text-light); font-weight: 300; }
  .badge-pct { fill: var(--accent-red); font-weight: 700; }
  .badge-label { fill: var(--text-light); font-weight: 700; }
  .ribbon-area { fill: url(#ribbon-tone); }
  .band-red { fill: var(--accent-red); }
  .band-white { fill: var(--accent-white); }
</style>
</head>
<body>
<div class="package">

  <svg class="package-spine" viewBox="0 0 110 1000" aria-label="Package side panel">
    <rect class="spine-bg" width="110" height="1000"/>
    <g transform="translate(42 230) rotate(-90)">
      <text class="tagline-bold" font-size="27" text-anchor="middle">100%</text>
      <text class="badge-label" font-size="14" y="20" text-anchor="middle">REMI HAIR</text>
    </g>
    <g transform="translate(66 470) rotate(-90)" text-anchor="middle">
      <text font-size="28"><tspan class="tagline-bold">HIGHEST</tspan><tspan class="tagline-light"> QUALITY</tspan></text>
    </g>
    <g transform="translate(64 770) rotate(-90)">
      <text class="brand-name" font-size="34" text-anchor="middle">Velvet Strands</text>
    </g>
    <rect class="band-red" y="962" width="110" height="20"/>
    <rect class="band-white" x="18" y="962" width="14" height="20"/>
    <rect class="band-white" x="64" y="962" width="14" height="20"/>
  </svg>

  <svg class="package-front" viewBox="0 0 440 1000" aria-label="Package front panel">
    <defs>
      <radialGradient id="hair-tone" cx="50%" cy="45%" r="60%">
        <stop offset="0" stop-color="#4a3442"/>
        <stop offset="1" stop-color="#241820"/>
      </radialGradient>
      <linearGradient id="ribbon-tone" x1="0" y1="0" x2="0" y2="1">
        <stop offset="0" stop-color="#141a21"/>
        <stop offset="0.5" stop-color="#3a2630"/>
        <stop offset="1" stop-color="#141a21"/>
      </linearGradient>
    </defs>
    <rect class="panel-bg" width="440" height="1000"/>

    <g class="brand-block">
      <circle cx="220" cy="150" r="20" fill="none" stroke="var(--text-light)" stroke-width="3"/>
      <text class="brand-name" x="220" y="250" font-size="52" text-anchor="middle">Velvet Strands</text>
    </g>

    <rect class="ribbon-area" x="0" y="280" width="440" height="110" role="img" aria-label="Flowing red, white and navy ribbon decoration"/>

    <g class="remi-badge">
      <circle cx="350" cy="390" r="40" fill="var(--wave-dark)" stroke="var(--accent-white)" stroke-width="3"/>
      <text class="badge-pct" x="350" y="392" font-size="21" text-anchor="middle">100%</text>
      <text class="badge-label" x="350" y="410" font-size="10.5" text-anchor="middle">REMI HAIR</text>
    </g>

    <text x="218" y="490" font-size="36" text-anchor="middle"><tspan class="tagline-bold">HIGHEST</tspan><tspan class="tagline-light"> QUALITY</tspan></text>

    <rect class="ribbon-area" x="0" y="520" width="440" height="120" role="img" aria-label="Flowing red, white and navy ribbon decoration"/>

    <circle cx="222" cy="760" r="104" fill="url(#hair-tone)" stroke="var(--accent-white)" stroke-width="6" role="img" aria-label="Window showing dark curly hair extension"/>

    <text x="220" y="935" font-size="28" text-anchor="middle"><tspan class="tagline-bold">NO</tspan><tspan class="tagline-light"> TANGLE </tspan><tspan class="tagline-bold">NO</tspan><tspan class="tagline-light"> DRY</tspan></text>

    <rect class="band-red" y="962" width="440" height="20"/>
  </svg>

</div>
</body>
</html>
```